Quillaro - Adventurous, Fun, Exciting, Social Fitness Club needs a Webpage with attitude!

Quillaro... we're a fun, social, outdoor fitness club that needs not just a homepage designed for our website, but in the process a "personality" for our unique, innovative and cheeky brand.
We pride ourselves on getting our members outdoors trying new, exciting physical activities in an effort to find joy in an active lifestyle, and sharing that experience with other like minded people. We offer:
- Personal Training (1-on-1 Fitness Training)
- Group Fitness Classes (Boxing, Pilates, etc)
- Boot Camps (Military Style - Sandbags, Ropes, Tyres, etc)
- Events (Fun Runs, Triathlons, Ocean Swims, Treks, etc)
- Adventures(Machu Picchu Trek, Rock Climbing, Kayaking, etc)
Our tag line is 'No Judgements. No Limits!' The homepage should be exciting, adventurous and innovative, illustrating the values of our brand: possibility, thirst for life, personal accomplishment & freedom. It should be fun, friendly & inviting.
A few of our key benefits to members are:
- No Boring Workouts
- No Joining Fees or Long Term Contracts
- Results Guaranteed
The links below should give you a rough idea of the sort of "feel" we're after (vibrant, active, adventurous ).
http://www.pupiljourneys.com.au/
http://www.layoutgoblin.com/website-templates/31924.html
http://www.layoutgoblin.com/website-templates/32751.html
http://www.pivel.com/
Target Market(s)
Real, Everyday People - Men & Women (30:70) aged mainly between 21-40, who want a more exciting and enjoyable fitness experience than your typical gym offers.
Industry/Entity Type
Fitness
Requirements
Must have
- Strong, uplifting and motivating images of people enjoying fitness/physical activities outdoors

```html
<!DOCTYPE html>
<html lang="en">
<head>
<meta charset="utf-8">
<title>Quillaro – Fitness Club</title>
<link href="https://fonts.googleapis.com/css2?family=Arimo:wght@400;700&display=swap" rel="stylesheet">
<style>
:root{
  --yellow:#f8c51c;
  --amber:#f4a21d;
  --orange:#ef7a22;
  --red:#e0452a;
  --black:#050505;
  --text:#333;
  --white:#fff;
}
*{box-sizing:border-box;margin:0;padding:0}
html,body{width:1117px;height:1200px;overflow:hidden;background:var(--white)}
body{font-family:"Arimo",Arial,sans-serif;color:var(--text)}
.page{position:absolute;left:0;top:0;width:1024px;height:1100px;transform:scale(1.0908);transform-origin:0 0}
.abs{position:absolute}

/* header */
.site-header{left:24px;top:8px;width:979px;height:200px;border-radius:14px;overflow:hidden;
  background:linear-gradient(180deg,var(--yellow) 0%,var(--amber) 25%,var(--orange) 40%,var(--red) 48%,var(--red) 100%);
  box-shadow:2px 3px 4px rgba(0,0,0,.35)}
.brand{left:20px;top:50px;display:flex;align-items:center;gap:12px}
.brand-dot{width:26px;height:26px;border-radius:50%;background:var(--black)}
.brand-name{font-size:52px;font-weight:700;color:var(--black);letter-spacing:1px}
.call{right:30px;top:10px;display:flex;align-items:center;gap:10px;color:var(--white);font-size:30px;text-shadow:1px 1px 2px rgba(0,0,0,.4)}
.call b{font-weight:700}
.call-icon{width:60px;height:60px}
.quick-links{right:32px;top:98px;display:flex;gap:30px}
.quick-link{display:flex;align-items:center;gap:8px;color:var(--white);font-weight:700;font-size:14px}
.quick-link svg{width:48px;height:48px}
.main-nav{left:0;bottom:0;width:100%;height:43px;display:flex;
  background:linear-gradient(180deg,#6a6a6a 0%,#2a2a2a 45%,#000 55%,#111 100%)}
.main-nav a{color:var(--white);font-weight:700;font-size:12px;text-decoration:none;display:flex;align-items:center;justify-content:center;border-right:1px solid #777}
.main-nav a.active{background:linear-gradient(180deg,var(--amber),var(--red))}

/* hero */
.hero{left:24px;top:224px;width:979px;height:316px;border-radius:14px;background:linear-gradient(180deg,var(--yellow),var(--amber))}
.hero-photo{left:8px;top:8px;width:661px;height:299px;border-radius:12px;overflow:hidden;border:1px solid #fff;
  background:linear-gradient(120deg,#d8d3cc 0%,#efe9e1 40%,#a79c8f 75%,#3d5a8a 100%)}
.hero-caption{left:0;top:135px;width:420px;height:164px;background:linear-gradient(90deg,rgba(0,0,0,.72) 70%,rgba(0,0,0,0));color:var(--white);padding:10px 16px}
.hero-caption h1{font-size:24px;font-weight:700;margin-bottom:10px}
.hero-caption h2{font-size:14px;font-weight:700;margin:0 4px 8px}
.hero-caption p{font-size:12px;line-height:14.5px;margin:0 4px 14px;width:360px;white-space:nowrap}
.hero-caption strong{font-size:12px;margin-left:4px}
.slider-dots{right:32px;bottom:7px;display:flex;gap:4px}
.slider-dots span{width:16px;height:16px;border-radius:50%;background:#000;border:2px solid #fff}
.slider-dots span.on{background:var(--red)}

.join{left:678px;top:8px;width:292px;height:299px;border-radius:12px;border:1px solid #fff;
  background:linear-gradient(180deg,#777 0%,#2c2c2c 20%,#000 40%,#000 100%);color:var(--white)}
.join h3{text-align:center;font-size:20px;font-weight:700;line-height:24px;margin-top:6px}
.join h3 em{font-style:normal;color:var(--yellow)}
.join-avatar{left:28px;top:66px;width:60px;height:72px;border-radius:12px;background:linear-gradient(180deg,var(--amber),var(--red))}
.perks{left:102px;top:66px;width:150px;list-style:none;font-size:12px;line-height:12px}
.perks li{margin-bottom:12px;padding-left:10px;position:relative}
.perks li::before{content:"»";position:absolute;left:0}
.field{left:30px;display:flex;align-items:center;font-size:12px}
.field label{width:45px}
.field span{width:156px;height:20px;background:linear-gradient(180deg,#ddd,#fff)}
.btn{display:flex;align-items:center;justify-content:center;color:var(--white);font-weight:700;font-size:11px;border-radius:8px;
  background:linear-gradient(180deg,var(--amber),var(--red));box-shadow:0 1px 2px rgba(0,0,0,.5)}
.join .btn{left:141px;top:261px;width:90px;height:26px}

/* services */
.service{top:551px;width:321px;height:225px;border-radius:6px;background:var(--black);overflow:hidden;box-shadow:2px 3px 4px rgba(0,0,0,.3)}
.service h4{height:37px;font-size:18px;font-weight:400;color:var(--white);padding:8px 16px;background:linear-gradient(180deg,var(--orange),var(--red))}
.service-photo{left:8px;top:44px;width:306px;height:88px;border-radius:12px;border:1px solid #fff}
.service p{left:9px;top:151px;font-size:12px;color:var(--white);white-space:nowrap}
.service p em{font-style:normal;color:var(--yellow)}
.service .btn{top:187px;height:26px}

/* welcome */
.welcome{left:28px;top:790px;width:742px}
.welcome h2{font-size:24px;font-weight:400;color:#000;margin-bottom:6px}
.welcome h2 b{color:var(--red)}
.welcome p{font-size:11.6px;line-height:14.5px;margin-bottom:14px;letter-spacing:-0.05px}
.welcome h3{font-size:13px;font-weight:700;margin:-4px 0 6px}
.video{left:777px;top:794px;width:226px;height:216px;border-radius:12px;background:var(--amber);padding:10px 6px 12px}
.video-frame{position:relative;width:100%;height:100%;border-radius:4px;background:linear-gradient(160deg,#cfd8dc 0%,#eae6df 50%,#b9c4c9 100%)}
.video-frame svg{position:absolute;left:72px;top:64px;width:78px;height:78px}

/* footer */
.site-footer{left:24px;top:1044px;width:973px;height:38px;border-radius:12px;display:flex;align-items:center;justify-content:center;
  background:linear-gradient(180deg,var(--yellow),var(--orange) 60%,var(--red));color:var(--white);font-size:11px;box-shadow:2px 3px 4px rgba(0,0,0,.3)}
</style>
</head>
<body>
<div class="page">

<header class="site-header abs">
  <div class="brand abs"><span class="brand-dot"></span><span class="brand-name">Quillaro</span></div>
  <div class="call abs">
    <svg class="call-icon" viewBox="0 0 60 60"><circle cx="30" cy="30" r="28" fill="#e0452a" stroke="#f8a060" stroke-width="3"/><path d="M22 16c3-1 5 6 3 8l-2 2c1 4 5 9 9 10l2-2c2-2 9 0 8 3l-1 3c-2 3-8 2-14-4s-8-13-5-16z" fill="#fff"/></svg>
    <span><b>Call</b> 1300 555 019</span>
  </div>
  <nav class="quick-links abs">
    <span class="quick-link"><svg viewBox="0 0 48 48"><circle cx="20" cy="20" r="17" fill="#fff" stroke="#5b8fc9" stroke-width="3"/><path d="M20 9v11l7 5" stroke="#333" stroke-width="2" fill="none"/><rect x="24" y="24" width="20" height="20" fill="#fff" stroke="#4caf50" stroke-width="2"/></svg>Time Table</span>
    <span class="quick-link"><svg viewBox="0 0 48 48"><path d="M4 12l13-4 14 4 13-4v30l-13 4-14-4-13 4z" fill="#8bc34a" stroke="#fff" stroke-width="2"/><path d="M24 6a7 7 0 0 1 7 7c0 6-7 13-7 13s-7-7-7-13a7 7 0 0 1 7-7z" fill="#e53935"/></svg>Club Locations</span>
    <span class="quick-link"><svg viewBox="0 0 48 48"><circle cx="18" cy="12" r="8" fill="none" stroke="#ccc" stroke-width="4"/><path d="M18 20v22l4-3v-3l-3-2 3-2" stroke="#bbb" stroke-width="4" fill="none"/></svg>Login</span>
  </nav>
  <nav class="main-nav abs">
    <a class="active" style="width:80px">Home</a>
    <a style="width:90px">About Us</a>
    <a style="width:84px">Fitness</a>
    <a style="width:157px">Events &amp; Adventures</a>
    <a style="width:100px;border:none">Contact Us</a>
  </nav>
</header>

<section class="hero abs">
  <div class="hero-photo abs" role="img" aria-label="People exercising together in a bright studio">
    <div class="hero-caption abs">
      <h1>Title Goes Here</h1>
      <h2>Subtitle Comes here</h2>
      <p>Lorem ipsum dolor sit amet consecutor. Lorem ipsum dolor sit<br>amet consecutor. Lorem ipsum dolor sit amet consecutor.<br>Lorem ipsum dolor sit amet consecutor.</p>
      <strong>Lorem ipsum dolor</strong>
    </div>
    <div class="slider-dots abs"><span class="on"></span><span></span><span></span><span></span><span></span></div>
  </div>
  <aside class="join abs">
    <h3><em>FREE</em> Membership,<br>Join Us: (<em>valued $65</em>)</h3>
    <div class="join-avatar abs" role="img" aria-label="Member illustration"></div>
    <ul class="perks abs">
      <li>Monthly E-News Hints, Tips &amp; Advice</li>
      <li>VIP Invites Events &amp; Adventures</li>
      <li>Special Member Only Offers</li>
      <li>Discount Card to 20+ Providers</li>
    </ul>
    <div class="field abs" style="top:207px"><label>Name:</label><span></span></div>
    <div class="field abs" style="top:233px"><label>Emai:</label><span></span></div>
    <div class="btn abs">Join Us</div>
  </aside>
</section>

<article class="service abs" style="left:24px">
  <h4>Personal Training</h4>
  <div class="service-photo abs" role="img" aria-label="Trainers in a weights gym" style="background:linear-gradient(90deg,#8a8a8a,#d6d6d6 60%,#fff)"></div>
  <p class="abs">Free initial Consult &amp; 1-on-1 Session (<em>valued $80.00</em>)</p>
  <div class="btn abs" style="left:224px;width:89px">More</div>
</article>
<article class="service abs" style="left:353px">
  <h4>Group Fitness</h4>
  <div class="service-photo abs" role="img" aria-label="Group stretching class" style="background:linear-gradient(90deg,#efe6dc,#d9c7e0 50%,#efe6dc)"></div>
  <p class="abs">Intro Pass <em>$25</em> 7 Days Unlimited Classes</p>
  <div class="btn abs" style="left:224px;width:89px">More</div>
</article>
<article class="service abs" style="left:682px">
  <h4>Boot Camp</h4>
  <div class="service-photo abs" role="img" aria-label="Outdoor boot camp jumping exercise" style="background:linear-gradient(180deg,#3f5a3a,#6f8a5e 55%,#b8b5a8)"></div>
  <p class="abs">Starts soon #'s Limited</p>
  <div class="btn abs" style="left:130px;width:89px">More Info</div>
  <div class="btn abs" style="left:224px;width:89px">Enlist</div>
</article>

<section class="welcome abs">
  <h2>Welcome to <b>QUILLARO</b></h2>
  <p>Lorem ipsum dolor sit amet consecutor. Lorem ipsum dolor sit amet consecutor. Lorem ipsum dolor sit amet consecutor. Lorem ipsum dolor sit amet consecutor. Lorem ipsum dolor sit amet consecutor. Lorem ipsum dolor sit amet consecutor. Lorem ipsum dolor sit amet consecutor. Lorem ipsum dolor sit amet consecutor. Lorem ipsum dolor sit amet consecutor.. Lorem ipsum dolor sit amet consecutor. Lorem ipsum dolor sit amet consecutor. Lorem ipsum dolor sit amet consecutor. Lorem ipsum dolor sit amet consecutor.</p>
  <h3>Lorem ipsum dolor</h3>
  <p>Lorem ipsum dolor sit amet consecutor. Lorem ipsum dolor sit amet consecutor. Lorem ipsum dolor sit amet consecutor. Lorem ipsum dolor sit amet consecutor. Lorem ipsum dolor sit amet consecutor. Lorem ipsum dolor sit amet consecutor. Lorem ipsum dolor sit amet consecutor. Lorem ipsum dolor sit amet consecutor. Lorem ipsum dolor sit amet consecutor.. Lorem ipsum dolor sit amet consecutor. Lorem ipsum dolor sit amet consecutor. Lorem ipsum dolor sit amet consecutor. Lorem ipsum dolor sit amet consecutor.</p>
  <p>Lorem ipsum dolor sit amet consecutor. Lorem ipsum dolor sit amet consecutor. Lorem ipsum dolor sit amet consecutor. Lorem ipsum dolor sit amet consecutor. Lorem ipsum dolor sit amet consecutor. Lorem ipsum dolor sit amet consecutor. Lorem ipsum dolor sit amet consecutor. Lorem ipsum dolor sit amet consecutor. Lorem ipsum dolor sit amet consecutor.</p>
</section>

<div class="video abs">
  <div class="video-frame" role="img" aria-label="Woman doing push-ups outdoors, promotional video">
    <svg viewBox="0 0 78 78"><circle cx="39" cy="39" r="35" fill="rgba(120,120,120,.55)" stroke="#555" stroke-width="5"/><path d="M30 22v34l28-17z" fill="#6d6d6d" stroke="#444" stroke-width="2"/></svg>
  </div>
</div>

<footer class="site-footer abs">Quillaro ©&nbsp; 2011 All Rights Reserved &nbsp;|&nbsp; Privacy Policy</footer>

</div>
</body>
</html>
```